Vorta Session Pass

**DESIGNERS PLEASE READ BRIEF, the ONES that were SUBMITTED does NOT HAVE THE REQUIREMENTS WE ASKED FOR

WE need a card that has the following:

- our LOGO
-Business info (email,phone,website etc)
- SMALL icons (either 3,5,10,15,20) where we can punch a hole to show how many classes our customers have attended
- a place to write the clients name and date of when they paid for the session pass
-an area to write - "This card is valid for the person who's name is on the front only and for a period of 8-40 weeks from date of purchase."

Front of card:
- Logo
- Session number and price" Can be redeemed with any class, check our schedule online.
- website:www.quellomotion.net.au
- Session hole punches (kettlebells or dumbbells)
- Name and date
- "Outdoor Group Fitness Classes"
Back of card:
- Vorta Logo and KESN logo
- email:info@quellomotion.net.au
- phone:0473 926 504
- Address: Pellbrook Oval, Marrowdale. Tarrant Creek Way/Holloway Dr
- Session number and price per session

I've attached our logo and the pricing for our classes.
I request the 20 class pass be made first just to ensure it all fits in well then we can look to delete boxes or kettlebells to adjust to the smaller class passes accordingly down the track. General colours we are thinking is black and green to match our logo and a stencil font or something similar.

Thanks in advance guys.
Updates

Please read project overview. We require a loyalty card/session pass card. So each time a client comes to one of our sessions we need to punch a hole in the card to indicate that they have come. We would like a design for a 20 session pass card made first. Can you utilize a kettle bell or dumbbell for indicating 20 sessions and we will punch a hole in them. We want the Vorta logo central on front and back, KESN logo on the back. All info in initial overview and request. Hope this makes sense, regards Glen.

Industry/Entity Type

Business

Requirements
Must have
• - SMALL icons (either 3,5,10,15,20) where we can punch a hole to show how many classes our customers have attended

```html
<!DOCTYPE html>
<html lang="en">
<head>
<meta charset="utf-8">
<title>Vorta Session Pass</title>
<link href="https://fonts.googleapis.com/css2?family=Oswald:wght@400;600;700&family=Open+Sans:wght@400;600&display=swap" rel="stylesheet">
<style>
  :root {
    --canvas: #ecebe8;
    --white: #ffffff;
    --ink: #1e1e1e;
    --green: #35b34a;
    --green-light: #6cc24a;
    --green-dark: #238b36;
    --grey-cell: #dcdcdc;
    --grey-punch: #9a9a9a;
    --rule: #2a2a2a;
  }
  * { box-sizing: border-box; margin: 0; padding: 0; }
  html, body { width: 1200px; height: 1024px; overflow: hidden; background: var(--canvas); }
  body { display: flex; flex-direction: column; align-items: center; justify-content: center; gap: 36px; font-family: "Open Sans", sans-serif; color: var(--ink); }

  .card { width: 760px; height: 464px; border-radius: 6px; box-shadow: 0 6px 20px rgba(0,0,0,.18); position: relative; overflow: hidden; }

  /* front */
  .card-front { background: var(--white); padding: 26px 30px; }
  .front-header { display: flex; justify-content: space-between; align-items: center; height: 104px; }
  .brand { display: flex; align-items: center; gap: 14px; }
  .brand-dot { width: 58px; height: 58px; border-radius: 50%; background: var(--green); }
  .brand-name { font-family: "Oswald", sans-serif; font-weight: 700; font-size: 32px; line-height: 1; letter-spacing: 2px; color: var(--green); text-transform: uppercase; }
  .brand-name span { display: block; }
  .tagline { text-align: right; font-family: "Oswald", sans-serif; font-weight: 700; }
  .tagline-title { font-size: 22px; }
  .tagline-web { font-size: 28px; letter-spacing: .5px; }
  .tagline-web em { font-style: normal; color: var(--green); }

  .session-table { width: 100%; border-collapse: collapse; margin-top: 14px; font-family: "Oswald", sans-serif; }
  .session-table th { background: var(--green); color: var(--ink); font-weight: 400; font-size: 17px; height: 34px; border: 2px solid var(--rule); }
  .session-table td { height: 36px; border: 2px solid var(--rule); font-size: 17px; text-align: center; }
  .session-table .col-name { width: 270px; }
  .session-table .col-date { width: 250px; }
  .session-table .cell-count { background: var(--grey-cell); width: 92px; }
  .session-table .cell-punch { background: var(--grey-punch); width: 70px; }
  .session-table th.cell-punch { background: var(--grey-punch); }
  .punch-hole { display: inline-block; width: 20px; height: 20px; border-radius: 50%; background: var(--white); border: 2px solid var(--rule); vertical-align: middle; }

  .validity { margin-top: 22px; text-align: center; font-size: 19px; line-height: 1.45; }

  /* back */
  .card-back { background: linear-gradient(160deg, var(--green-light) 0%, var(--green) 55%, var(--green-dark) 100%); color: var(--white); padding: 34px 34px; display: flex; justify-content: space-between; }
  .back-info { width: 340px; }
  .card-back .brand-dot { background: var(--white); }
  .card-back .brand-name { color: var(--white); }
  .contact-list { list-style: none; margin-top: 34px; font-size: 17px; }
  .contact-list li { display: flex; align-items: flex-start; gap: 12px; margin-bottom: 14px; line-height: 1.35; }
  .contact-list svg { flex: 0 0 20px; width: 20px; height: 20px; margin-top: 2px; }

  .pricing { width: 340px; align-self: flex-start; margin-top: 30px; }
  .pricing-table { width: 100%; border-collapse: collapse; font-family: "Oswald", sans-serif; font-size: 16px; color: var(--ink); }
  .pricing-table td, .pricing-table th { border: 2px solid var(--rule); padding: 4px 8px; }
  .pricing-table .pricing-title { background: var(--white); font-size: 21px; font-weight: 600; text-align: center; }
  .pricing-table .casual { background: var(--green); color: var(--white); text-align: center; }
  .pricing-table tr.row-white td { background: var(--white); }
  .pricing-table tr.row-green td { background: var(--green); color: var(--white); }
  .partner-badge { position: absolute; right: 40px; bottom: 30px; width: 84px; height: 84px; border-radius: 50%; border: 3px solid var(--white); }
</style>
</head>
<body>

<section class="card card-front" aria-label="Session pass front">
  <header class="front-header">
    <div class="brand">
      <div class="brand-dot"></div>
      <div class="brand-name"><span>Vorta</span><span>Fitness</span></div>
    </div>
    <div class="tagline">
      <p class="tagline-title">“Outdoor Group Fitness Classes”</p>
      <p class="tagline-web">WWW.<em>QUELLOMOTION</em>.NET.AU</p>
    </div>
  </header>

  <table class="session-table">
    <tr>
      <th class="col-name">Name</th>
      <th class="col-date">Date</th>
      <th class="cell-count">Sessions</th>
      <th class="cell-punch"></th>
    </tr>
    <tr><td></td><td></td><td class="cell-count">3</td><td class="cell-punch"><span class="punch-hole"></span></td></tr>
    <tr><td></td><td></td><td class="cell-count">5</td><td class="cell-punch"><span class="punch-hole"></span></td></tr>
    <tr><td></td><td></td><td class="cell-count">10</td><td class="cell-punch"><span class="punch-hole"></span></td></tr>
    <tr><td></td><td></td><td class="cell-count">15</td><td class="cell-punch"><span class="punch-hole"></span></td></tr>
    <tr><td></td><td></td><td class="cell-count">20</td><td class="cell-punch"><span class="punch-hole"></span></td></tr>
  </table>

  <p class="validity">This card is valid for the person who's name is on the front only and for<br>a period of 8-40 weeks from date of purchase.</p>
</section>

<section class="card card-back" aria-label="Session pass back">
  <div class="back-info">
    <div class="brand">
      <div class="brand-dot"></div>
      <div class="brand-name"><span>Vorta</span><span>Fitness</span></div>
    </div>
    <ul class="contact-list">
      <li>
        <svg viewBox="0 0 24 24" fill="#fff"><path d="M6.6 10.8a15 15 0 0 0 6.6 6.6l2.2-2.2a1 1 0 0 1 1-.25 11.4 11.4 0 0 0 3.6.57 1 1 0 0 1 1 1V20a1 1 0 0 1-1 1A17 17 0 0 1 3 4a1 1 0 0 1 1-1h3.5a1 1 0 0 1 1 1c0 1.250.2 2.45.57 3.57a1 1 0 0 1-.25 1z"/></svg>
        <span>0473 926 504</span>
      </li>
      <li>
        <svg viewBox="0 0 24 24" fill="#fff"><path d="M3 5h18v14H3z" opacity=".9"/><path d="M3 5l9 7 9-7" fill="none" stroke="#35b34a" stroke-width="2"/></svg>
        <span>info@quellomotion.net.au</span>
      </li>
      <li>
        <svg viewBox="0 0 24 24" fill="none" stroke="#fff" stroke-width="2"><circle cx="12" cy="12" r="9"/><path d="M3 12h18M12 3c3 3 3 15 0 18M12 3c-3 3-3 15 0 18"/></svg>
        <span>www.quellomotion.net.au</span>
      </li>
      <li>
        <svg viewBox="0 0 24 24" fill="#fff"><path d="M12 2a7 7 0 0 0-7 7c0 5 7 13 7 13s7-8 7-13a7 7 0 0 0-7-7zm0 9.5A2.5 2.5 0 1 1 12 6.5a2.5 2.5 0 0 1 0 5z"/></svg>
        <span>Pellbrook Oval, Marrowdale.<br>Tarrant Creek Way/Holloway Dr</span>
      </li>
    </ul>
  </div>

  <div class="pricing">
    <table class="pricing-table">
      <tr><th class="pricing-title" colspan="2">Vorta Fitness Pricing</th></tr>
      <tr><td class="casual" colspan="2">Casual - $12</td></tr>
      <tr class="row-white"><td>3 Session Pass</td><td>$30 ($10 a class)</td></tr>
      <tr class="row-green"><td>5 Session Pass</td><td>$45 ($9 a class)</td></tr>
      <tr class="row-white"><td>10 Session Pass</td><td>$80 ($8 a class)</td></tr>
      <tr class="row-green"><td>15 Session Pass</td><td>$105 ($7 a class)</td></tr>
      <tr class="row-white"><td>20 Session Pass</td><td>$120 ($6 a class)</td></tr>
    </table>
  </div>

  <div class="partner-badge" role="img" aria-label="Partner badge"></div>
</section>

</body>
</html>
```